Business cards for Norwegian software consultancy business

We are in need of business cards for our Norwegian consultancy company.
“Vilma Tronsoft AS” specializes in software development, architecture and agile methodology, providing mostly on-site services at customers.
The cards should reflect a certain level of business professionalism with an elegant touch, while paying tribute to our modern and technological heritage. Our logo should be featured, as well as room for basic information about the cardholder and legal information of the company (company name, address and VAT number).
We would like our cards to reflect that we are a modern consulting company. It should present a professional image that people will remember. The texture and color pallette should reflect our professionalism and reliability, so we prefer a light color pallette with colors such as gray, white, blue and black. The number of colors used should however not be overwhelming, with the text being distinct and readable.
We are open to untraditional layouts and playful designs as long as they communicate the intent stated above.
You could also take a look at our website http://www.tronsoft-demo.no for input on our visual profile.
Our logo is attached in the form of vectors and rasterized PNG. Please comment if you would like the black-white and/or inverted versions as well.
Architecture
Company information:
Vilma Tronsoft AS
Lindåsgata 7, 3129 Nøtterøy
481 62 509
info@tronsoft-demo.no
www.tronsoft-demo.no
Employee information:
Full name
Title
Email
Phone

```html
<!DOCTYPE html>
<html lang="no">
<head>
<meta charset="utf-8">
<title>Vilma Tronsoft AS – Business Card</title>
<link rel="stylesheet" href="https://fonts.googleapis.com/css2?family=Questrial&display=swap">
<style>
  :root {
    --page-bg: #eceef1;
    --card-white: #ffffff;
    --blue-light: #e9eff9;
    --blue-mid: #9fb6e2;
    --blue-deep: #4f97d3;
    --blue-accent: #5a9ad6;
    --slate: #6b7a8b;
    --slate-light: #a2afbd;
    --ink: #1f2226;
  }
  * { box-sizing: border-box; margin: 0; padding: 0; }
  html, body {
    width: 1200px;
    height: 1200px;
    overflow: hidden;
    background: var(--page-bg);
    font-family: "Questrial", "Century Gothic", sans-serif;
  }
  .card {
    position: absolute;
    left: 260px;
    top: 60px;
    width: 680px;
    height: 1080px;
    overflow: hidden;
    background: var(--card-white);
    box-shadow: 0 10px 30px rgba(30, 40, 60, 0.18);
  }
  .card__pattern {
    position: absolute;
    inset: 0;
    width: 680px;
    height: 1080px;
  }
  .brand {
    position: absolute;
    left: 222px;
    top: 405px;
    display: flex;
    align-items: center;
    gap: 16px;
  }
  .brand__mark {
    width: 40px;
    height: 40px;
    background: var(--blue-accent);
  }
  .brand__name {
    font-size: 36px;
    color: var(--ink);
    letter-spacing: 0.5px;
    white-space: nowrap;
  }
  .contact {
    position: absolute;
    left: 78px;
    top: 770px;
    list-style: none;
  }
  .contact__item {
    display: flex;
    align-items: center;
    gap: 28px;
    height: 72px;
    font-size: 25px;
    color: var(--ink);
    line-height: 1.2;
  }
  .contact__item--address { height: 92px; }
  .contact__icon {
    width: 34px;
    height: 34px;
    flex: none;
    fill: var(--blue-accent);
  }
</style>
</head>
<body>
  <main class="card">
    <svg class="card__pattern" viewBox="0 0 680 1080" aria-hidden="true">
      <defs>
        <linearGradient id="field" x1="0" y1="0" x2="0.3" y2="1">
          <stop offset="0" stop-color="#f4f7fc"/>
          <stop offset="0.5" stop-color="#b9cbea"/>
          <stop offset="1" stop-color="#4f97d3"/>
        </linearGradient>
        <linearGradient id="hex-top" x1="0" y1="0" x2="0.4" y2="1">
          <stop offset="0" stop-color="#b6c6e8"/>
          <stop offset="1" stop-color="#7f9bd6"/>
        </linearGradient>
        <linearGradient id="hex-slate" x1="0" y1="0" x2="0" y2="1">
          <stop offset="0" stop-color="#6b7a8b"/>
          <stop offset="1" stop-color="#a2afbd"/>
        </linearGradient>
      </defs>
      <rect class="pattern__field" width="680" height="1080" fill="url(#field)"/>
      <polygon class="pattern__hex pattern__hex--top" points="470,60 320,320 20,320 -130,60 20,-200 320,-200" fill="url(#hex-top)"/>
      <polygon class="pattern__hex pattern__hex--slate" points="1000,1000 900,1173 720,1173 620,1000 720,827 900,827" fill="url(#hex-slate)"/>
      <polygon class="pattern__hex pattern__hex--logo" points="780,430 630,690 330,690 180,430 330,170 630,170" fill="#ffffff"/>
      <polygon class="pattern__hex pattern__hex--contact" points="590,990 430,1267 110,1267 -50,990 110,713 430,713" fill="#ffffff"/>
    </svg>

    <div class="brand">
      <span class="brand__mark"></span>
      <span class="brand__name">Vilma Tronsoft AS</span>
    </div>

    <ul class="contact">
      <li class="contact__item contact__item--address">
        <svg class="contact__icon" viewBox="0 0 24 24" aria-hidden="true"><path d="M12 2a7 7 0 0 0-7 7c0 5 7 13 7 13s7-8 7-13a7 7 0 0 0-7-7zm0 9.5A2.5 2.5 0 1 1 12 6.5a2.5 2.5 0 0 1 0 5z"/></svg>
        <span>Lindåsgata 7<br>3129 Nøtterøy</span>
      </li>
      <li class="contact__item">
        <svg class="contact__icon" viewBox="0 0 24 24" aria-hidden="true"><path d="M6.6 10.8a15 15 0 0 0 6.6 6.6l2.2-2.2a1 1 0 0 1 1-.25 11.4 11.4 0 0 0 3.6.57 1 1 0 0 1 1 1V20a1 1 0 0 1-1 1A17 17 0 0 1 3 4a1 1 0 0 1 1-1h3.5a1 1 0 0 1 1 1c0 1.25.2 2.45.57 3.57a1 1 0 0 1-.25 1z"/></svg>
        <span>481 62 509</span>
      </li>
      <li class="contact__item">
        <svg class="contact__icon" viewBox="0 0 24 24" aria-hidden="true"><path d="M2 5h20v14H2z M3.5 6.5 12 13l8.5-6.5" fill="none" stroke="#5a9ad6" stroke-width="1.6"/><path d="M2 5h20L12 12.5z"/></svg>
        <span>info@tronsoft-demo.no</span>
      </li>
      <li class="contact__item">
        <svg class="contact__icon" viewBox="0 0 24 24" aria-hidden="true"><g fill="none" stroke="#5a9ad6" stroke-width="1.6"><circle cx="12" cy="12" r="9.5"/><ellipse cx="12" cy="12" rx="4.2" ry="9.5"/><path d="M2.5 12h19M4 7h16M4 17h16M12 2.5v19"/></g></svg>
        <span>www.tronsoft-demo.no</span>
      </li>
    </ul>
  </main>
</body>
</html>
```